E-commerce Website needs category banner

What we need for our category banner is a clean, predominately black design that showcases the product we are trying to sell (currently only 1), and a few subtle gradients that follow the pattern set by previous designs.

An example will be provided to showcase what we want.

It needs to say:
Outdoor Motion Detection Lighting in large, clear font similar to the example provided.

Please ensure dimensions are as follows: 980x300

Target Market(s)

Senior citizens, businesses, homeowners, families, etc

Industry/Entity Type

Product

Font styles to use
Sans Serif

Requirements
Must have
• It needs to say:
Outdoor Motion Detection Lighting in large, clear font similar to the example provided
980x300 is the required size!
Should not have
• Too much going on- clean and simple please (no crazy fonts, logos, etc)

```html
<!DOCTYPE html>
<html lang="en">
<head>
<meta charset="UTF-8">
<title>Outdoor Motion Detection Lighting</title>
<link rel="stylesheet" href="https://fonts.googleapis.com/css2?family=Teko:wght@500&display=swap">
<style>
  :root {
    --bg-center: #4b4b4b;
    --bg-mid: #262626;
    --bg-edge: #060606;
    --type-top: #ffffff;
    --type-bottom: #c9c9c9;
    --type-shadow: rgba(0, 0, 0, 0.85);
    --product-light: #f4f4f2;
    --product-mid: #d9d9d6;
    --product-dark: #9a9a97;
  }
  html, body {
    margin: 0;
    padding: 0;
    overflow: hidden;
    background: #000;
  }
  .category-banner {
    position: relative;
    width: 1200px;
    height: 367px;
    overflow: hidden;
    background:
      radial-gradient(ellipse 70% 95% at 62% 50%, var(--bg-center) 0%, var(--bg-mid) 55%, var(--bg-edge) 100%);
  }
  .banner-title {
    position: absolute;
    left: 34px;
    top: 50px;
    margin: 0;
    font-family: "Teko", "Arial Narrow", sans-serif;
    font-weight: 500;
    font-size: 128px;
    line-height: 104px;
    letter-spacing: 0;
    white-space: nowrap;
    text-transform: uppercase;
    transform: scaleX(0.78);
    transform-origin: left top;
    color: var(--type-top);
    background: linear-gradient(180deg, var(--type-top) 0%, var(--type-top) 45%, var(--type-bottom) 100%);
    -webkit-background-clip: text;
    background-clip: text;
    -webkit-text-fill-color: transparent;
    filter: drop-shadow(2px 3px 2px var(--type-shadow));
  }
  .banner-title .title-line {
    display: block;
  }
  .product-shot {
    position: absolute;
    border-radius: 44% 44% 38% 38%;
    background:
      radial-gradient(ellipse 60% 55% at 40% 35%, var(--product-light) 0%, var(--product-mid) 60%, var(--product-dark) 100%);
    box-shadow: 0 10px 24px rgba(0, 0, 0, 0.45);
  }
  .product-shot--front {
    left: 746px;
    top: 28px;
    width: 192px;
    height: 258px;
  }
  .product-shot--side {
    left: 958px;
    top: 30px;
    width: 190px;
    height: 256px;
  }
</style>
</head>
<body>
  <section class="category-banner">
    <h1 class="banner-title">
      <span class="title-line">Outdoor Motion</span>
      <span class="title-line">Detection Lighting</span>
    </h1>
    <div class="product-shot product-shot--front" role="img" aria-label="White wireless LED motion sensor spotlight with two LEDs and a sensor, on a wall mount, front view"></div>
    <div class="product-shot product-shot--side" role="img" aria-label="White wireless LED motion sensor spotlight on a wall mount, angled view"></div>
  </section>
</body>
</html>
```